Bref créative
Business Cards for Young Professional
Professional, edgy, modern, credible, smart.
Professional
Doran Whitlake
Owner
4627 Mesa Lorna, NW
Albuquerque, NM 87309
dorenw@velbrik.example
velbrik.example
I plan to have cards printed on paper. But some will be made by metal etching. These metal cards will have a small area to be filled with melted brazing metal. I will attach pictures to demonstrate this principal.

```html
<!DOCTYPE html>
<html lang="en">
<head>
<meta charset="utf-8">
<title>Velbrik Consolidated — Business Cards</title>
<link href="https://fonts.googleapis.com/css2?family=Michroma&display=swap" rel="stylesheet">
<style>
  :root {
    --page: #e4e5e7;
    --paper: #ffffff;
    --blue: #1a3fb0;
    --blue-deep: #0d2a8a;
    --silver-light: #eef0f3;
    --silver-dark: #9ea3aa;
    --ink: #1f2a66;
    --white: #ffffff;
  }
  html, body {
    margin: 0;
    width: 1200px;
    height: 895px;
    overflow: hidden;
    background: var(--page);
    font-family: "Michroma", sans-serif;
  }
  .canvas {
    position: relative;
    width: 1200px;
    height: 895px;
  }
  .card {
    position: absolute;
    top: 293px;
    width: 540px;
    height: 309px;
    background: var(--paper);
    box-shadow: 0 4px 14px rgba(0,0,0,0.12);
    overflow: hidden;
  }
  .card-front { left: 40px; }
  .card-back { left: 620px; }
  .card-art { position: absolute; inset: 0; }

  .brand {
    position: absolute;
    display: flex;
    align-items: center;
    gap: 12px;
  }
  .brand-dot {
    width: 44px;
    height: 44px;
    border-radius: 50%;
    background: var(--blue);
    flex: none;
  }
  .brand-name {
    color: var(--ink);
    font-size: 15px;
    letter-spacing: 0.5px;
    line-height: 1;
  }
  .brand-tagline {
    color: var(--ink);
    font-size: 7px;
    letter-spacing: 4px;
    margin-top: 5px;
    text-align: center;
  }
  .card-front .brand { left: 30px; top: 30px; }

  .holder {
    position: absolute;
    left: 190px;
    top: 178px;
    color: var(--white);
  }
  .holder-name { font-size: 12px; letter-spacing: 1px; }
  .holder-role { font-size: 8px; margin-top: 4px; text-align: right; letter-spacing: 1px; }

  .address {
    position: absolute;
    left: 30px;
    top: 222px;
    color: var(--white);
    font-size: 8.5px;
    line-height: 1.75;
    letter-spacing: 0.5px;
  }
  .contact {
    position: absolute;
    left: 290px;
    top: 218px;
    color: var(--white);
    font-size: 8.5px;
    letter-spacing: 0.5px;
    list-style: none;
    margin: 0;
    padding: 0 0 0 14px;
    border-left: 1px solid rgba(255,255,255,0.6);
  }
  .contact li {
    display: flex;
    align-items: center;
    gap: 8px;
    height: 17px;
  }
  .contact svg { width: 11px; height: 11px; flex: none; }

  .card-back .brand {
    left: 50%;
    top: 50%;
    transform: translate(-50%, -50%);
    flex-direction: column;
    gap: 10px;
  }
  .card-back .brand-dot { width: 70px; height: 70px; }
  .back-web {
    position: absolute;
    left: 34px;
    top: 154px;
    transform: translate(-50%, -50%) rotate(90deg);
    color: var(--ink);
    font-size: 9px;
    letter-spacing: 6px;
    white-space: nowrap;
  }
</style>
</head>
<body>
<main class="canvas">

  <section class="card card-front" aria-label="Card front">
    <svg class="card-art" viewBox="0 0 540 309" aria-hidden="true">
      <defs>
        <linearGradient id="silverBand" x1="0" y1="0" x2="1" y2="0">
          <stop offset="0" stop-color="var(--silver-dark)"/>
          <stop offset="0.5" stop-color="var(--silver-light)"/>
          <stop offset="1" stop-color="var(--silver-dark)"/>
        </linearGradient>
        <linearGradient id="blueField" x1="0" y1="0" x2="0" y2="1">
          <stop offset="0" stop-color="var(--blue)"/>
          <stop offset="1" stop-color="var(--blue-deep)"/>
        </linearGradient>
      </defs>
      <path d="M0,128 C180,168 360,118 540,92 L540,132 C360,150 180,190 0,170 Z" fill="url(#silverBand)"/>
      <path d="M0,160 C180,192 360,148 540,124 L540,309 L0,309 Z" fill="url(#blueField)"/>
    </svg>

    <div class="brand">
      <span class="brand-dot"></span>
      <div>
        <div class="brand-name">VELBRIK CONSOLIDATED</div>
        <div class="brand-tagline">ENGINEERING</div>
      </div>
    </div>

    <div class="holder">
      <div class="holder-name">Doran Whitlake</div>
      <div class="holder-role">Owner</div>
    </div>

    <div class="address">
      4627 Mesa Lorna, NW<br>
      Albuquerque,<br>
      NM 87309
    </div>

    <ul class="contact">
      <li>
        <svg viewBox="0 0 12 12"><circle cx="6" cy="6" r="6" fill="#fff"/><path d="M4 3.2l1 1.6-.6.6a4 4 0 0 0 2.2 2.2l.6-.6 1.6 1-.6 1C6 8.8 3.2 6 3 4z" fill="var(--blue)"/></svg>
        505-555-0148
      </li>
      <li>
        <svg viewBox="0 0 12 12"><circle cx="6" cy="6" r="6" fill="#fff"/><rect x="3" y="4" width="6" height="4.2" fill="none" stroke="var(--blue)" stroke-width="0.9"/><path d="M3 4l3 2.3L9 4" fill="none" stroke="var(--blue)" stroke-width="0.9"/></svg>
        dorenw@velbrik.example
      </li>
      <li>
        <svg viewBox="0 0 12 12"><circle cx="6" cy="6" r="6" fill="#fff"/><circle cx="6" cy="6" r="2.4" fill="var(--blue)"/></svg>
        Pelimarker
      </li>
      <li>
        <svg viewBox="0 0 12 12"><circle cx="6" cy="6" r="6" fill="#fff"/><circle cx="6" cy="6" r="3" fill="none" stroke="var(--blue)" stroke-width="0.9"/><path d="M3 6h6M6 3v6" stroke="var(--blue)" stroke-width="0.7"/></svg>
        www.velbrik.example
      </li>
    </ul>
  </section>

  <section class="card card-back" aria-label="Card back">
    <div class="back-web">WWW.VELBRIK.EXAMPLE</div>
    <div class="brand">
      <span class="brand-dot"></span>
      <div class="brand-name">VELBRIK CONSOLIDATED</div>
    </div>
  </section>

</main>
</body>
</html>
```